Design some Business Cards for Varnek Electrical Services Pty Ltd.

Attached is a logo for Varnek Electrical Services Pty Ltd. Also is attached a template I would like to have a similar design/font/Colour scheme.

```html
<!DOCTYPE html>
<html lang="en">
<head>
<meta charset="utf-8">
<title>Varnek Electrical Services – Business Cards</title>
<link href="https://fonts.googleapis.com/css2?family=Open+Sans:wght@400;600;700&display=swap" rel="stylesheet">
<style>
  :root {
    --bg: #e4e5e7;
    --blue: #2a45a3;
    --blue-deep: #1e3587;
    --green: #4caf3c;
    --white: #ffffff;
    --paper: #f3f4f6;
    --ink: #2c3c8c;
    --shadow: rgba(20, 30, 60, 0.22);
  }
  html, body {
    margin: 0;
    padding: 0;
    width: 1200px;
    height: 936px;
    overflow: hidden;
    background: var(--bg);
    font-family: "Open Sans", Arial, sans-serif;
  }
  .stage {
    position: relative;
    width: 1200px;
    height: 936px;
    background: radial-gradient(ellipse at 50% 40%, #f4f4f5 0%, var(--bg) 70%);
  }
  .card {
    position: absolute;
    width: 520px;
    height: 300px;
    border-radius: 22px;
    overflow: hidden;
    box-shadow: 0 14px 30px var(--shadow);
  }
  .card--back {
    left: 80px;
    top: 190px;
    background: linear-gradient(160deg, var(--blue) 0%, var(--blue-deep) 100%);
  }
  .card--front {
    left: 600px;
    top: 440px;
    background: var(--paper);
  }
  .card__shapes {
    position: absolute;
    inset: 0;
  }
  .brand {
    position: absolute;
    display: flex;
    align-items: center;
    gap: 10px;
  }
  .brand__dot {
    width: 18px;
    height: 18px;
    border-radius: 50%;
    background: var(--green);
    flex: none;
  }
  .brand__name {
    color: var(--white);
    font-weight: 600;
    font-size: 17px;
    line-height: 1.25;
    letter-spacing: 0.5px;
  }
  .card--back .brand {
    left: 50%;
    top: 104px;
    transform: translateX(-50%);
    width: 300px;
    justify-content: center;
  }
  .card--back .brand__name { font-size: 19px; }
  .web-rule {
    position: absolute;
    left: 40px;
    right: 40px;
    top: 196px;
    display: flex;
    align-items: center;
    gap: 12px;
    color: var(--white);
    font-size: 12px;
  }
  .web-rule::before,
  .web-rule::after {
    content: "";
    flex: 1;
    height: 1px;
    background: linear-gradient(90deg, rgba(255,255,255,0), rgba(255,255,255,0.7), rgba(255,255,255,0));
  }
  .card--front .brand {
    left: 34px;
    top: 128px;
    width: 200px;
  }
  .person {
    position: absolute;
    right: 26px;
    top: 30px;
    text-align: right;
  }
  .person__name {
    margin: 0;
    color: var(--green);
    font-weight: 700;
    font-size: 21px;
    letter-spacing: 0.5px;
    white-space: nowrap;
  }
  .person__role {
    margin: 2px 0 0;
    color: var(--ink);
    font-size: 13px;
  }
  .contact {
    position: absolute;
    left: 300px;
    top: 124px;
    color: var(--ink);
    font-size: 11px;
    line-height: 1.55;
    white-space: nowrap;
  }
  .contact__company {
    font-weight: 700;
    font-size: 11px;
  }
  .contact__list {
    list-style: none;
    margin: 6px 0 0;
    padding: 0;
  }
  .contact__list li {
    display: flex;
    align-items: center;
    gap: 7px;
  }
  .contact__icon {
    width: 11px;
    height: 11px;
    flex: none;
  }
</style>
</head>
<body>
<main class="stage">

  <section class="card card--back" aria-label="Business card back">
    <div class="brand">
      <span class="brand__dot"></span>
      <span class="brand__name">Varnek Electrical Services Pty Ltd</span>
    </div>
    <div class="web-rule">www.varnekelectrical.com.au</div>
  </section>

  <section class="card card--front" aria-label="Business card front">
    <svg class="card__shapes" viewBox="0 0 520 300" preserveAspectRatio="none" aria-hidden="true">
      <defs>
        <linearGradient id="frontBlue" x1="0" y1="0" x2="1" y2="1">
          <stop offset="0" stop-color="#2a45a3"/>
          <stop offset="1" stop-color="#1e3587"/>
        </linearGradient>
      </defs>
      <path d="M296 0 H312 C260 64 270 156 220 222 C190 260 158 286 138 300 H120 C152 280 180 252 202 214 C248 150 242 60 296 0 Z" fill="#4caf3c"/>
      <path d="M0 0 H280 C230 60 242 150 200 210 C175 250 150 280 112 300 H0 Z" fill="url(#frontBlue)"/>
    </svg>

    <div class="brand">
      <span class="brand__dot"></span>
      <span class="brand__name">Varnek Electrical Services Pty Ltd</span>
    </div>

    <div class="person">
      <h2 class="person__name">MARCUS DELANEY</h2>
      <p class="person__role">Ceo &amp; Founder</p>
    </div>

    <div class="contact">
      <div class="contact__company">Varnek Electrical Service Pty Ltd</div>
      <div>PO Box 812 Lindale VA 20471</div>
      <ul class="contact__list">
        <li>
          <svg class="contact__icon" viewBox="0 0 12 12" aria-hidden="true"><rect x="3" y="0.5" width="6" height="11" rx="1.2" fill="none" stroke="#2c3c8c" stroke-width="1.2"/><circle cx="6" cy="9.5" r="0.7" fill="#2c3c8c"/></svg>
          <span>(000) 482 917 365</span>
        </li>
        <li>
          <svg class="contact__icon" viewBox="0 0 12 12" aria-hidden="true"><rect x="0.6" y="2" width="10.8" height="8" rx="1" fill="none" stroke="#2c3c8c" stroke-width="1.2"/><path d="M1 2.6 L6 6.6 L11 2.6" fill="none" stroke="#2c3c8c" stroke-width="1.2"/></svg>
          <span>mail@varnekelectrical.com.au</span>
        </li>
        <li>
          <svg class="contact__icon" viewBox="0 0 12 12" aria-hidden="true"><circle cx="6" cy="6" r="5.2" fill="none" stroke="#2c3c8c" stroke-width="1.1"/><ellipse cx="6" cy="6" rx="2.3" ry="5.2" fill="none" stroke="#2c3c8c" stroke-width="1"/><line x1="0.8" y1="6" x2="11.2" y2="6" stroke="#2c3c8c" stroke-width="1"/></svg>
          <span>www.varnekelectrical.com.au</span>
        </li>
      </ul>
    </div>
  </section>

</main>
</body>
</html>
```